The Red Ember Masa Kitchen

I would like your designers to design a clean business card with information I provide for my business , website is theredembermasakitchen.example and the email is rlpadilla14@mailbox.example , I would like for you to use the two tamales I send, that is my logo if you can fix it up that would be great, I am also open to any other options that you can come up with , thank you

```html
<!DOCTYPE html>
<html lang="en">
<head>
<meta charset="utf-8">
<title>The Red Ember Masa Kitchen – Business Cards</title>
<link href="https://fonts.googleapis.com/css2?family=Great+Vibes&family=Open+Sans:wght@400&display=swap" rel="stylesheet">
<style>
  :root {
    --backdrop: #d9d9d9;
    --card: #0b0b0b;
    --ember: #f26a21;
    --ember-deep: #d9531a;
    --ink-light: #f4f4f4;
    --ink-soft: #cfcfcf;
  }
  * { box-sizing: border-box; margin: 0; padding: 0; }
  html, body { width: 1200px; height: 1000px; overflow: hidden; }
  body {
    background: var(--backdrop);
    position: relative;
    font-family: "Great Vibes", cursive;
    color: var(--ink-light);
  }
  .card {
    position: absolute;
    background: var(--card);
    box-shadow: 0 6px 14px rgba(0,0,0,0.35);
  }

  /* Menu card (portrait) */
  .menu-card {
    left: 90px; top: 150px;
    width: 420px; height: 720px;
    text-align: center;
    padding-top: 44px;
  }
  .brand-mark {
    display: block;
    margin: 0 auto;
    border-radius: 50%;
    background: radial-gradient(circle at 40% 40%, var(--ember), var(--ember-deep));
  }
  .menu-card .brand-mark { width: 90px; height: 90px; }
  .brand-name {
    color: var(--ember);
    font-size: 44px;
    line-height: 1.0;
    font-weight: 400;
  }
  .menu-card .brand-name { margin-top: 16px; }
  .tagline {
    font-family: "Open Sans", sans-serif;
    font-size: 13px;
    color: var(--ink-light);
    margin-top: 8px;
  }
  .menu-list { margin-top: 30px; }
  .menu-group { margin-bottom: 26px; }
  .menu-heading {
    color: var(--ember);
    font-size: 28px;
    line-height: 1.1;
  }
  .menu-items {
    color: var(--ink-light);
    font-size: 27px;
    line-height: 1.15;
  }

  /* Contact card (landscape) */
  .contact-card {
    left: 560px; top: 310px;
    width: 580px; height: 380px;
    padding: 36px 40px;
  }
  .contact-brand {
    display: flex;
    align-items: center;
    gap: 26px;
  }
  .contact-card .brand-mark { width: 110px; height: 110px; margin: 0; flex: none; }
  .contact-card .brand-name { font-size: 46px; }
  .contact-list {
    list-style: none;
    margin-top: 34px;
    font-size: 30px;
    line-height: 1.2;
  }
  .contact-label { color: var(--ember); }
  .contact-value { color: var(--ink-light); }
</style>
</head>
<body>

  <section class="card menu-card">
    <span class="brand-mark" role="img" aria-label="Brand mark area"></span>
    <h1 class="brand-name">The Red Ember<br>Masa Kitchen</h1>
    <p class="tagline">Home of Homemade Tamale and Salsa</p>

    <div class="menu-list">
      <div class="menu-group">
        <h2 class="menu-heading">Tamales:</h2>
        <p class="menu-items">Pork, Chicken, Beef, Veggie<br>(Beans, Cheese &amp; Jalapeño)</p>
      </div>
      <div class="menu-group">
        <h2 class="menu-heading">Dessert Tamale:</h2>
        <p class="menu-items">Strawberry, Pineapple, Aple, Cherry,<br>Peach etc.</p>
      </div>
      <div class="menu-group">
        <h2 class="menu-heading">Breakfast Tamale:</h2>
        <p class="menu-items">Eggs &amp; Chorizo, Ham Egg &amp; Cheese,<br>Veggie Omlete etc.</p>
      </div>
      <div class="menu-group">
        <h2 class="menu-heading">Salsa:</h2>
        <p class="menu-items">Verde (Green), Rojo (Red)</p>
      </div>
    </div>
  </section>

  <section class="card contact-card">
    <div class="contact-brand">
      <span class="brand-mark" role="img" aria-label="Brand mark area"></span>
      <div>
        <h1 class="brand-name">The Red Ember<br>Masa Kitchen</h1>
        <p class="tagline">Home of Homemade Tamale and Salsa</p>
      </div>
    </div>
    <ul class="contact-list">
      <li><span class="contact-label">Phone:</span> <span class="contact-value">(555) 218-3047</span></li>
      <li><span class="contact-label">Cell:</span> <span class="contact-value">(555) 604-1195</span></li>
      <li><span class="contact-label">Email:</span> <span class="contact-value">rlpadilla14@mailbox.example</span></li>
      <li><span class="contact-label">Website:</span> <span class="contact-value">theredembermasakitchen.example</span></li>
    </ul>
  </section>

</body>
</html>
```